web design for specialty coffee shop

We are online shop selling specialty coffeee.
Our brand concept keywords are -
specialty coffee, knowledge, discovery, professional, convenience, collaboration.
there will be five main tabs on the homepage
[home (u icon from logo)]
[coffee]
[equipment]
[gift]
[knowledge]
[about us]
For our site, we will be using the following template.
ONLY DESIGN, NO CODING necessary as our developers will do that.
http://plendrixthemes.net/item/velmora-premium-responsive-shopcart-theme/full_screen_preview/7302514
Use the template as a base.
You do not have to do exactly the same layout.
Creative Liberty!
For the style and color palette, please look at the attached image.
Our brown logo should match nicely with the style provided in the attachment.
Thank you for taking the time to read this post.
Looking forward to working with artquivery and the amazing designers that are part of this community.
Reason: Dear designers,
I have extended the deadline to give designers who accepted to participate in this contest some more time to submit their designs. Thank you for understanding.
Coffee Shop

```html
<!DOCTYPE html>
<html lang="en">
<head>
<meta charset="utf-8">
<title>Kindra Coffee Lab</title>
<link rel="stylesheet" href="https://fonts.googleapis.com/css2?family=Arimo:wght@400;700&family=Cinzel:wght@700&display=swap">
<style>
:root{
  --band:#8a6a4e;
  --page:#e4d2b8;
  --white:#ffffff;
  --ink:#3a3a3a;
  --body:#555555;
  --brown:#7c5a3b;
  --shop:#7a4b2f;
  --logo:#2f3337;
  --orange:#f47b20;
  --orange-dark:#e0621a;
  --frame:#efe5d8;
  --bar:#e3e3e3;
  --rule:#cfcfcf;
  --price:#c62a1f;
  --title:#e0621a;
  --fb:#3b5a9a;
  --yellow:#f6b51b;
}
*{box-sizing:border-box;margin:0;padding:0}
html,body{width:1107px;height:1200px;overflow:hidden}
body{background:var(--page);font-family:"Arimo",Arial,sans-serif;color:var(--body)}
.canvas{position:relative;width:1107px;height:1200px;overflow:hidden;background:var(--page)}
.top-band{position:absolute;left:0;top:0;width:1107px;height:160px;background:var(--band)}
.sheet{position:absolute;left:83px;top:97px;width:941px;height:1018px;background:var(--white)}
.abs{position:absolute}
.logo{left:95px;top:11px;width:212px;height:167px;z-index:10;background:var(--logo);box-shadow:0 3px 6px rgba(0,0,0,.35);display:flex;flex-direction:column;align-items:center;justify-content:center;color:var(--white)}
.logo-mark{width:26px;height:26px;border:3px solid var(--white);border-radius:50%;margin-bottom:16px}
.logo-name{font-size:44px;font-weight:700;line-height:1}
.logo-sub{font-size:15px;letter-spacing:4px;margin-top:4px}
.btn-orange{background:var(--orange);color:var(--white);font-size:14px;font-weight:700;height:27px;line-height:27px;text-align:center;border:1px solid var(--orange-dark)}
.connect{left:713px;top:55px;width:105px;height:27px;background:var(--fb);border:1px solid #2b4478;border-radius:3px;color:var(--white);font-size:14px;font-weight:700;display:flex;align-items:center;gap:14px;padding-left:8px}
.connect i{display:block;width:14px;height:14px;background:var(--white);opacity:.85}
.cart{left:826px;top:11px;width:197px;height:73px;background:#f5efe6;border:2px solid #f19a5a;display:flex;align-items:center}
.cart svg{margin:0 8px 0 12px}
.cart-info{border-left:1px solid #e2cdb5;padding-left:10px;height:56px}
.cart-title{color:var(--orange-dark);font-size:12px;margin-top:2px}
.cart-items{color:#666;font-size:12px;margin-top:3px}
.checkout{margin-top:5px;width:90px;height:20px;border-radius:10px;background:var(--yellow);color:var(--white);font-size:10px;font-weight:700;line-height:20px;padding-left:10px}
.nav-bar{left:87px;top:101px;width:932px;height:58px;background:#f6f1eb}
.nav{left:343px;top:121px;display:flex;gap:40px;font-family:"Cinzel",Georgia,serif;font-weight:700;font-size:15px;color:var(--ink);letter-spacing:.2px}
.nav .active{color:var(--shop)}
.search{left:869px;top:116px;width:146px;height:27px;background:var(--white);border:1px solid #ccc;font-size:11px;color:#333;padding:7px 8px;display:flex;justify-content:space-between}
.hero-frame{left:87px;top:160px;width:932px;height:424px;background:var(--frame)}
.hero{left:95px;top:169px;width:917px;height:406px;background:radial-gradient(ellipse at 72% 55%,#dcdad6 0,#b9a797 22%,#9a7557 45%,#6e4a31 75%,#3a2416 100%)}
.hero-title{left:118px;top:225px;font-family:"Cinzel",Georgia,serif;font-weight:700;font-size:29px;color:var(--white)}
.hero-text{left:117px;top:270px;width:437px;font-size:14px;line-height:20px;color:var(--white)}
.book{left:116px;top:363px;width:203px;height:46px;background:linear-gradient(#55595d,#2f3337);border:1px solid #222;border-radius:3px;color:var(--white);font-size:18px;font-weight:700;display:flex;align-items:center;justify-content:center;gap:10px}
.book span{width:16px;height:16px;border-radius:50%;background:#6b6f73;font-size:11px;line-height:16px;text-align:center}
.slide-arrow{top:534px;width:29px;height:29px;border-radius:50%;border:2px solid #ddd;background:rgba(255,255,255,.25);color:var(--white);font-size:15px;text-align:center;line-height:25px}
.col{top:604px;width:299px}
.col-head{display:flex;align-items:center;gap:14px;height:40px;border-bottom:1px solid var(--rule);padding-bottom:6px;font-family:"Cinzel",Georgia,serif;font-weight:700;font-size:21px;color:var(--brown)}
.col-text{margin-top:10px;font-size:13px;line-height:19.3px;text-align:justify;color:var(--body)}
.view-more{margin-top:12px;height:34px;background:var(--bar);font-family:"Cinzel",Georgia,serif;font-weight:700;font-size:13px;color:#777;text-align:right;padding:10px 14px 0 0}
.sep{left:91px;top:794px;width:924px;height:1px;background:var(--rule)}
.coffee-head{left:91px;top:820px;display:flex;align-items:center;gap:16px;font-family:"Cinzel",Georgia,serif;font-weight:700;font-size:21px;color:var(--brown)}
.next{left:997px;top:824px;width:18px;height:18px;border-radius:50%;background:#aaa;color:var(--white);font-size:11px;text-align:center;line-height:18px}
.card{top:862px;width:299px;height:140px;border:2px solid #e4e4e4;display:flex;padding:14px 0 0 18px}
.card-img{width:80px;height:100px;border-radius:3px}
.card-info{margin-left:26px;font-size:13px;line-height:17px}
.card-title{color:var(--title);font-size:14px}
.card-price{color:var(--price);margin:11px 0 10px}
.card-desc{color:var(--body);width:165px}
.press{left:91px;top:1025px;width:924px;height:82px;background:var(--bar);display:flex;align-items:center;justify-content:space-around;padding:0 30px;font-size:20px;font-weight:700;color:#555}
.footer-links{left:82px;top:1135px;font-size:12px;color:#555;word-spacing:2px}
.copyright{left:82px;top:1164px;font-size:12px;color:#555}
.pay{top:1148px;width:28px;height:18px;background:var(--white);border:1px solid #ccc;border-radius:2px}
.social{top:1144px;width:24px;height:24px;border-radius:50%;background:#b6a48e}
</style>
</head>
<body>
<div class="canvas">
  <div class="top-band"></div>
  <div class="sheet"></div>

  <div class="abs btn-orange" style="left:683px;top:16px;width:63px">LOG IN</div>
  <div class="abs btn-orange" style="left:752px;top:16px;width:68px">SIGN UP</div>
  <div class="abs connect"><i></i>Connect</div>

  <div class="abs cart">
    <svg width="50" height="46" viewBox="0 0 50 46" fill="none" stroke="#b8a99a" stroke-width="3">
      <path d="M2 6h8l6 24h26l5-18H13"/><circle cx="20" cy="39" r="3" fill="#b8a99a"/><circle cx="38" cy="39" r="3" fill="#b8a99a"/>
    </svg>
    <div class="cart-info">
      <div class="cart-title">MY CART</div>
      <div class="cart-items">(0) items - $00.00</div>
      <div class="checkout">CHECKOUT ›</div>
    </div>
  </div>

  <div class="abs nav-bar"></div>
  <nav class="abs nav">
    <span class="active">SHOP</span><span>SUBSCRIPTION</span><span>GIFT</span><span>KNOWLEDGE</span><span>FAQ</span>
  </nav>
  <div class="abs search"><span>Search</span>
    <svg width="14" height="14" viewBox="0 0 14 14"><circle cx="5.5" cy="5.5" r="4" fill="none" stroke="#222" stroke-width="2"/><path d="M8.5 8.5l4 4" stroke="#222" stroke-width="2.5"/></svg>
  </div>

  <div class="abs logo">
    <div class="logo-mark"></div>
    <div class="logo-name">kindra</div>
    <div class="logo-sub">coffee lab</div>
  </div>

  <div class="abs hero-frame"></div>
  <div class="abs hero" role="img" aria-label="Steaming white cup of coffee on a saucer with roasted coffee beans on burlap"></div>
  <h1 class="abs hero-title">WELCOME TO KINDRA</h1>
  <p class="abs hero-text">Nulla vel magna nec metus hendrerit blandit id sed justo. Duis egestas imperdiet quam, vitae vehicula diam aliquam a. Vivamus dictum ornare nulla. Nam convallis egestas libero. Vestibulum mi magna, ultrices ut port titor non, sagittis imperdiet metus.</p>
  <div class="abs book"><span>›</span>BOOK NOW</div>
  <div class="abs slide-arrow" style="left:117px">←</div>
  <div class="abs slide-arrow" style="left:151px">→</div>

  <section class="abs col" style="left:91px">
    <h2 class="col-head"><svg width="30" height="30"><rect x="3" y="3" width="24" height="24" fill="#2f3337"/></svg>ABOUT US</h2>
    <p class="col-text">Curabitur eu nibh eget nunc dictum feugiat at vel odio. Etiam in sapien et odio tincidunt porta. Pellentesque tempus magna ac lorem commodo laoreet. pellen-tesque suscipit pretium.</p>
    <div class="view-more">VIEW MORE</div>
  </section>
  <section class="abs col" style="left:404px">
    <h2 class="col-head"><svg width="30" height="32" viewBox="0 0 30 32"><path d="M11 2h8v10l9 18H2l9-18z" fill="#2f3337"/><rect x="9" y="1" width="12" height="3" fill="#2f3337"/></svg>KNOWLEDGE</h2>
    <p class="col-text">Curabitur eu nibh eget nunc dictum feugiat at vel odio. Etiam in sapien et odio tincidunt porta. Pellentesque tempus magna ac lorem commodo laoreet. pellen-tesque suscipit pretium.</p>
    <div class="view-more">VIEW MORE</div>
  </section>
  <section class="abs col" style="left:716px">
    <h2 class="col-head"><svg width="32" height="32" viewBox="0 0 32 32" fill="none" stroke="#2f3337" stroke-width="2.5"><ellipse cx="20" cy="10" rx="8" ry="6"/><ellipse cx="9" cy="20" rx="6" ry="8"/><ellipse cx="23" cy="25" rx="5" ry="4"/></svg>SUBSCRIPTION</h2>
    <p class="col-text">Curabitur eu nibh eget nunc dictum feugiat at vel odio. Etiam in sapien et odio tincidunt porta. Pellentesque tempus magna ac lorem commodo laoreet. pellen-tesque suscipit pretium.</p>
    <div class="view-more">VIEW MORE</div>
  </section>

  <div class="abs sep"></div>
  <h2 class="abs coffee-head"><svg width="32" height="26" viewBox="0 0 32 26"><rect x="8" y="2" width="22" height="22" rx="2" fill="#2f3337"/><path d="M8 7H3v11h5" fill="none" stroke="#2f3337" stroke-width="3"/></svg>OUR COFFEES</h2>
  <div class="abs next">›</div>

  <article class="abs card" style="left:91px">
    <div class="card-img" role="img" aria-label="Coffee bag with spilled beans and a cup" style="background:linear-gradient(160deg,#f2f0ec,#d9d4cc 60%,#8a6a4e)"></div>
    <div class="card-info"><div class="card-title">Proin rutrum magna</div><div class="card-price">Price : $19.00</div><div class="card-desc">Aenean sit amet nisl metus, ac hendrerit velit. Nunc urna lectus, cursusa.</div></div>
  </article>
  <article class="abs card" style="left:404px">
    <div class="card-img" role="img" aria-label="Kraft paper coffee bag" style="background:linear-gradient(#c9a57c,#a57c52)"></div>
    <div class="card-info"><div class="card-title">Proin rutrum magna</div><div class="card-price">Price : $19.00</div><div class="card-desc">Aenean sit amet nisl metus, ac hendrerit velit. Nunc urna lectus, cursusa.</div></div>
  </article>
  <article class="abs card" style="left:716px">
    <div class="card-img" role="img" aria-label="Kraft coffee bag with dark label" style="background:linear-gradient(#cfae88,#b08a62 45%,#2a2a2a 55%,#b08a62 75%)"></div>
    <div class="card-info"><div class="card-title">Proin rutrum magna</div><div class="card-price">Price : $19.00</div><div class="card-desc">Aenean sit amet nisl metus, ac hendrerit velit. Nunc urna lectus, cursusa.</div></div>
  </article>

  <div class="abs press">
    <span>Pantrywise</span><span>The Harbor Ledger</span><span>Brewnotes.com</span><span>Fork Report</span><span>Kitchen40</span><span>Good Plates</span>
  </div>

  <div class="abs footer-links">Home &nbsp;| &nbsp;Shop &nbsp;| &nbsp;Subscription &nbsp;| &nbsp;Gift &nbsp;| &nbsp;Knowledge &nbsp;| &nbsp;FAQ &nbsp;| &nbsp;Contact</div>
  <div class="abs copyright">Copyright &nbsp;© &nbsp;2013 &nbsp;&nbsp;www.kindracoffee.com &nbsp;&nbsp;All rights reserved.</div>

  <div class="abs pay" style="left:787px"></div>
  <div class="abs pay" style="left:822px"></div>
  <div class="abs pay" style="left:857px"></div>
  <div class="abs pay" style="left:892px"></div>
  <div class="abs pay" style="left:927px"></div>
  <div class="abs social" style="left:968px"></div>
  <div class="abs social" style="left:1000px"></div>
</div>
</body>
</html>
```